Professional Accounting Services Flyer

Attached is a publisher document and word document each containing the flyer text. This needs to be polished and improved to become an A4 2 sided marketing flyer.
It would be helpful if the design graphics on the flyer are in keeping with the product being sold, which is accounting and financial services.
The business in essence provides outsourced Chief Financial Office (CFO) services along with bookkeeping and a range of other accounting functions.

Target Market(s)

Small to Medium sized businesses requiring accounting support beyond the traditional preparation of tax returns

Industry/Entity Type

Accounting

Colors
0255a3
3277b5
85acd3
cedeed
ffffff
000000

Requirements
Must have
• The provided text
• Professional look and feel consistent with provision of professional accounting and financial services
• 2 sided A4 flyer
Nice to have
• Effective graphics which enhance the message and are in keeping with the theme of the business
Should not have
• Tacky or gimmicky looking graphics (please keep the graphics professional looking)
• A feel that indicates that tax return preparation is part of the business

```html
<!DOCTYPE html>
<html lang="en">
<head>
<meta charset="utf-8">
<title>Vertex Advisory – Two-Sided Flyer</title>
<link rel="stylesheet" href="https://fonts.googleapis.com/css2?family=Oswald:wght@500&family=Roboto+Condensed:wght@400;700&family=Open+Sans:ital,wght@0,400;0,600;1,400&display=swap">
<style>
:root{
  --blue-deep:#0255a3;
  --blue:#1a6fc0;
  --blue-mid:#3277b5;
  --blue-soft:#85acd3;
  --blue-pale:#cedeed;
  --white:#ffffff;
  --ink:#3a3a3a;
  --ink-dark:#1e1e1e;
  --yellow:#ffd21a;
  --backdrop:#8c8d91;
  --icon:#9aa3ad;
}
*{box-sizing:border-box;margin:0;padding:0}
html,body{width:1200px;height:814px;overflow:hidden}
body{background:var(--backdrop);position:relative;font-family:"Open Sans",Arial,sans-serif;color:var(--ink)}
.page{position:absolute;top:62px;width:529px;height:684px;background:var(--white);overflow:hidden}
.page--front{left:66px}
.page--back{left:625px}
.page__baseline{position:absolute;left:0;right:0;bottom:0;height:9px;background:var(--blue)}
.body-text{font-size:6.9px;line-height:10.3px}
.heading{font-family:"Roboto Condensed",Arial,sans-serif;font-weight:700;color:var(--blue)}
.heading--yellow{color:var(--yellow)}

/* front */
.hero{position:absolute;left:0;top:0;width:529px;height:260px}
.brand{position:absolute;left:250px;top:18px;display:flex;align-items:center;gap:8px}
.brand__dot{width:26px;height:26px;border-radius:50%;background:var(--blue)}
.brand__name{font-family:"Oswald",Arial,sans-serif;font-weight:500;font-size:28px;letter-spacing:.3px;color:var(--blue);line-height:1}
.tagline{position:absolute;right:38px;top:80px;text-align:right;font-family:"Roboto Condensed",Arial,sans-serif;font-size:22px;line-height:25px;color:var(--ink-dark);text-shadow:0 0 3px #fff,0 0 3px #fff}
.tagline__accent{color:var(--blue)}

.why{position:absolute;left:27px;top:234px;width:172px;height:264px;background:var(--blue);border-radius:0 0 16px 0;padding:14px 10px 0 18px;color:var(--white)}
.why__title{font-size:13.5px;line-height:15px;margin-bottom:9px}
.why p{font-weight:600;font-size:6.6px;line-height:10px;margin-bottom:6px}
.why__closing{font-style:italic;color:var(--yellow);font-weight:400 !important;font-size:7.2px !important}

.services{position:absolute;left:214px;top:279px;width:290px}
.service{position:relative;padding-left:36px;margin-bottom:9px}
.service__icon{position:absolute;left:0;top:2px;width:28px;height:28px}
.service__title{font-size:11px;line-height:13px}
.service p{color:var(--ink)}

.offer{position:absolute;left:40px;top:519px;width:160px}
.offer__title{font-size:12px;line-height:14.5px;font-weight:400;margin-bottom:10px}
.offer ul{list-style:none;font-size:7.3px;line-height:10.8px;padding-left:8px}
.offer li{position:relative;padding-left:12px}
.offer li::before{content:"";position:absolute;left:0;top:4px;width:3.5px;height:3.5px;border-radius:50%;background:var(--yellow)}

.contact{position:absolute;bottom:9px;height:55px;background:var(--blue);color:var(--white);padding:9px 0 0 38px}
.contact--front{left:0;width:199px;border-radius:0 14px 0 0}
.contact--back{right:0;width:259px;border-radius:14px 0 0 0;padding-left:85px}
.contact__title{font-size:11px;line-height:12px;font-weight:700;font-family:"Roboto Condensed",Arial,sans-serif;margin-bottom:2px}
.contact p{font-size:6.7px;line-height:9px}
.contact__mark{position:absolute;left:22px;top:9px;width:40px;height:40px;border-radius:50%;border:3px solid var(--white)}

/* back */
.about{position:absolute;left:20px;top:0;width:237px;height:249px;background:var(--blue);border-radius:0 0 14px 14px;padding:36px 14px 0 23px;color:var(--white)}
.about__title{font-size:13.5px;margin-bottom:7px}
.about p{font-size:6.7px;line-height:10.3px;margin-bottom:10px}
.faq-art{position:absolute;left:273px;top:0;width:256px;height:171px}
.team-art{position:absolute;left:10px;top:266px;width:247px;height:155px}
.management{position:absolute;left:29px;top:421px;width:206px}
.management__title{font-size:13px;margin-bottom:9px}
.management p{margin-bottom:9px;font-size:6.8px;line-height:10px}
.faq{position:absolute;left:271px;top:181px;width:238px}
.faq__title{font-size:13px;margin-bottom:11px}
.faq__item{margin-bottom:8px}
.faq__q{font-weight:600;color:var(--ink-dark);font-size:6.7px;line-height:9.5px}
.faq__a{font-size:6.7px;line-height:9.5px}
</style>
</head>
<body>

<section class="page page--front">
  <svg class="hero" viewBox="0 0 529 260">
    <defs>
      <linearGradient id="heroTone" x1="0" y1="0" x2="1" y2="1">
        <stop offset="0" stop-color="#cedeed"/>
        <stop offset=".45" stop-color="#e8eef4"/>
        <stop offset=".8" stop-color="#b9c6d2"/>
        <stop offset="1" stop-color="#d6dde4"/>
      </linearGradient>
      <linearGradient id="heroFade" x1="0" y1="0" x2="1" y2="0">
        <stop offset=".35" stop-color="#ffffff" stop-opacity="0"/>
        <stop offset=".8" stop-color="#ffffff" stop-opacity=".85"/>
      </linearGradient>
    </defs>
    <g role="img" aria-label="Photo: hand writing with a pen beside a calculator and coins">
      <path d="M0 0H529V215C430 250 300 262 200 255 120 250 50 236 0 222Z" fill="url(#heroTone)"/>
      <path d="M0 0H529V215C430 250 300 262 200 255 120 250 50 236 0 222Z" fill="url(#heroFade)"/>
    </g>
    <path d="M27 240C120 214 250 210 380 226 440 233 490 240 529 248V236C470 222 420 214 380 210 250 196 120 204 27 226Z" fill="var(--blue)"/>
  </svg>

  <div class="brand">
    <span class="brand__dot"></span>
    <span class="brand__name">VERTEX ADVISORY</span>
  </div>

  <div class="tagline">
    <div>PROVIDING</div>
    <div class="tagline__accent">OUTSOURCED SOLUTIONS</div>
    <div>TO YOUR BUSINESS</div>
  </div>

  <aside class="why">
    <h2 class="heading heading--yellow why__title">Why Choose<br>Vertex Advisory?</h2>
    <p>Are you experiencing significant growth and facing pressure to continue to successfully manage all aspects of your business?</p>
    <p>Do you find the day to day tasks of meeting your financial, accounting and company secretarial obligations is diverting your time from your core business?</p>
    <p>Is a lack of expert financial support holding your business back from achieving its potential?</p>
    <p>Are you considering listing, raising capital, or borrowing funds to achieve your business goals?</p>
    <p>Are you looking for cost effective solutions to improve your business performance?</p>
    <p class="why__closing">If this applies to you Vertex Advisory can help you achieve your goals.</p>
  </aside>

  <div class="services">
    <article class="service">
      <svg class="service__icon" viewBox="0 0 28 28"><circle cx="12" cy="8" r="5" fill="var(--icon)"/><path d="M3 26c0-7 4-11 9-11s9 4 9 11Z" fill="var(--icon)"/><circle cx="22" cy="19" r="4" fill="none" stroke="var(--icon)" stroke-width="1.5"/></svg>
      <h3 class="heading service__title">CFO Services</h3>
      <p class="body-text">Large companies utilise the services of a Chief Financial Officer (CFO) to manage the financial complexity of modern businesses. CFO services allows you to have access to the same skills on a part time basis. This function allows you to have a senior financial professional assist with managing activities</p>
    </article>
    <article class="service">
      <svg class="service__icon" viewBox="0 0 28 28"><rect x="3" y="14" width="22" height="3" fill="var(--icon)"/><rect x="5" y="17" width="2" height="9" fill="var(--icon)"/><rect x="18" y="17" width="6" height="9" fill="none" stroke="var(--icon)" stroke-width="1.5"/><rect x="8" y="4" width="10" height="8" fill="none" stroke="var(--icon)" stroke-width="1.5"/></svg>
      <h3 class="heading service__title">Company Secretarial Services</h3>
      <p class="body-text">We can provide secretarial services whether your business is a private company just requiring the basics or if you operate a small capital listed entity requiring the services of a Company Secretary to meet the obligations of the corporate regulator as well as the stock exchange.</p>
    </article>
    <article class="service">
      <svg class="service__icon" viewBox="0 0 28 28"><rect x="3" y="3" width="15" height="22" fill="none" stroke="var(--icon)" stroke-width="1.5"/><path d="M6 9h9M6 13h9M6 17h6" stroke="var(--icon)" stroke-width="1.5"/><rect x="16" y="12" width="10" height="14" fill="var(--white)" stroke="var(--icon)" stroke-width="1.5"/><path d="M18 16h6M18 19h6M18 22h6" stroke="var(--icon)" stroke-width="1.2"/></svg>
      <h3 class="heading service__title">Financial Reporting</h3>
      <p class="body-text">Whether you need to meet the expectations of banks or outside investors we can assist by providing the necessary skills to compile financial reports. Alternately you may need assistance meeting the tight deadlines associated with raising funds through debt and equity markets. We can provide this service along with assistance in the preparation of Prospectus documents or Information Memorandum. We are able to act as lead or provide supplemental support for an existing internal team.</p>
    </article>
    <article class="service">
      <svg class="service__icon" viewBox="0 0 28 28"><rect x="2" y="5" width="24" height="16" fill="none" stroke="var(--icon)" stroke-width="1.5"/><path d="M6 17v-4M9 17v-6M12 17v-3" stroke="var(--icon)" stroke-width="1.5"/><circle cx="18" cy="13" r="4" fill="none" stroke="var(--icon)" stroke-width="1.5"/><path d="M21 16l4 4" stroke="var(--icon)" stroke-width="2"/></svg>
      <h3 class="heading service__title">Forensic Accounting</h3>
      <p class="body-text">Everyone hopes their employees are honest and act with integrity, however, this is not always the case. If your business has been the subject of a suspected financial crime we can help. We can conduct a forensic review and where needed provide expert testimony should the matter lead to a court case.</p>
    </article>
    <article class="service">
      <svg class="service__icon" viewBox="0 0 28 28"><rect x="3" y="4" width="6" height="21" fill="none" stroke="var(--icon)" stroke-width="1.5"/><rect x="11" y="4" width="6" height="21" fill="none" stroke="var(--icon)" stroke-width="1.5"/><rect x="19" y="5" width="6" height="20" fill="none" stroke="var(--icon)" stroke-width="1.5" transform="rotate(-10 22 15)"/><path d="M4 18h4M12 18h4" stroke="var(--icon)" stroke-width="1.5"/></svg>
      <h3 class="heading service__title">Bookkeeping and Payroll</h3>
      <p class="body-text">These essential tasks form part of running every business but often take up an excessive amount of your valuable time. These tasks which are necessary can be performed by someone with the right skills allowing you to focus on the business. We can assist you with this enabling you to concentrate on the areas of your business that add the most value.</p>
    </article>
  </div>

  <div class="offer">
    <h2 class="heading offer__title">What Services Does Vertex Advisory Provide?</h2>
    <ul>
      <li>CFO services</li>
      <li>Company Secretarial services</li>
      <li>Financial Reporting</li>
      <li>Forensic Accounting</li>
      <li>Bookkeeping and Payroll</li>
    </ul>
  </div>

  <footer class="contact contact--front">
    <h2 class="contact__title">Contact us:</h2>
    <p>Phone: 0400 555 018</p>
    <p>Email: gwhitfield@vertexadvisory.example</p>
    <p>Mail: PO Box 200 HARBOURSIDE WA 6000</p>
  </footer>
  <div class="page__baseline"></div>
</section>

<section class="page page--back">
  <div class="about">
    <h2 class="heading heading--yellow about__title">About Vertex Advisory</h2>
    <p>Vertex Advisory is focused on delivering services to small and medium businesses which are often only available to larger businesses. At its core Vertex Advisory is focused on providing to small and medium businesses the key services large organisations gain through the employment of a dedicated CFO.</p>
    <p>These services will enable you to focus your efforts on growing your business and ensuring the operations are performing to achieve the goals you have set. Vertex Advisory is able to partner with you to ensure that as the business grows, the financial and governance needs continue to keep pace and enable growth to occur efficiently and effectively.</p>
    <p>With growth and size comes complexity and Vertex Advisory is able assist you in managing these risks allowing the business to thrive and develop successfully.</p>
  </div>

  <svg class="faq-art" viewBox="0 0 256 171" role="img" aria-label="Illustration: large blue FAQ lettering among grey question words">
    <defs>
      <radialGradient id="faqTone" cx=".45" cy=".45" r=".7">
        <stop offset="0" stop-color="#3277b5"/>
        <stop offset=".45" stop-color="#85acd3"/>
        <stop offset=".8" stop-color="#e4e8ec"/>
        <stop offset="1" stop-color="#ffffff"/>
      </radialGradient>
    </defs>
    <rect width="256" height="171" fill="url(#faqTone)"/>
  </svg>

  <svg class="team-art" viewBox="0 0 247 155" role="img" aria-label="Photo: silhouettes of business people standing in a bright office">
    <defs>
      <linearGradient id="teamTone" x1="0" y1="0" x2="0" y2="1">
        <stop offset="0" stop-color="#ffffff"/>
        <stop offset=".3" stop-color="#cedeed"/>
        <stop offset=".55" stop-color="#1f4f86"/>
        <stop offset=".8" stop-color="#85acd3"/>
        <stop offset="1" stop-color="#ffffff"/>
      </linearGradient>
    </defs>
    <rect width="247" height="155" fill="url(#teamTone)"/>
  </svg>

  <div class="management">
    <h2 class="heading management__title">Key Management</h2>
    <p>Graham Whitfield is at the heart of the business with over 25 years of experience gained across both public practice and commerce. Most of this experience has been gained working in a range of commercial organisations ranging in size from 100 staff through to organisations with over 10,000 employees. This has included senior financial positions within top 200 listed companies with operations both within Australia and operations overseas.</p>
    <p>Graham’s experience extends to a range of sectors, including retailing, wholesaling, mining and exploration, construction and manufacturing. This experience is particularly extensive within fast moving consumer goods and operational mines extracting gold, copper and coal.</p>
    <p>Graham has also been involved in a range of corporate activities including business acquisitions, stock exchange listings (particularly in Singapore), debt raisings and corporate demergers. Through these activities, he has been exposed to the debt and equity market regimes in Australia, Singapore and the United States of America.</p>
  </div>

  <div class="faq">
    <h2 class="heading faq__title">Frequently Asked Questions</h2>
    <div class="faq__item">
      <p class="faq__q">If I utilise the CFO services of Vertex Advisory, does that mean I don’t need to worry about the financials?</p>
      <p class="faq__a">Vertex Advisory acts as your personal CFO. Like any successful business the CEO must remain engaged with the financial health and prosperity of the business. What Vertex Advisory will do, is assist you in fully understanding this information and using financial information to drive your business forward.</p>
    </div>
    <div class="faq__item">
      <p class="faq__q">If I decide to raise capital or list my business on a stock exchange, can Vertex Advisory help me?</p>
      <p class="faq__a">Yes, there are a number of ways we can be of assistance. Vertex Advisory can act as your CFO and drive the process, including, managing the various aspects involved in raising capital and listing a company. If you already have internal resources but require additional help to achieve the outcome within the deadlines, Vertex Advisory can provide that assistance.</p>
    </div>
    <div class="faq__item">
      <p class="faq__q">Does Vertex Advisory provide taxation services?</p>
      <p class="faq__a">While Vertex Advisory does not provide taxation services, we are able to assist you through an associate who is a registered tax agent.</p>
    </div>
    <div class="faq__item">
      <p class="faq__q">Does Vertex Advisory conduct audit and assurance services?</p>
      <p class="faq__a">These services are not provided by Vertex Advisory, however there are a range of accounting firms we can direct you toward. We are also able to act in the same manner as a dedicated CFO would in engaging with these providers and managing the audit process should you require.</p>
    </div>
    <div class="faq__item">
      <p class="faq__q">Does Vertex Advisory provide expert opinions for debt and equity raisings or takeovers?</p>
      <p class="faq__a">These are specialised services which Vertex Advisory does not provide. However, we can manage the process on your behalf to achieve the outcomes required.</p>
    </div>
    <div class="faq__item">
      <p class="faq__q">Does Vertex Advisory provide Valuations?</p>
      <p class="faq__a">Vertex Advisory does not provide valuations, however, we are able to manage this process on your behalf or assist with collation of all relevant information to facilitate a valuation.</p>
    </div>
  </div>

  <footer class="contact contact--back">
    <span class="contact__mark"></span>
    <h2 class="contact__title">Contact us:</h2>
    <p>Phone: 0400 555 018</p>
    <p>Email: gwhitfield@vertexadvisory.example</p>
    <p>Mail: PO Box 200 HARBOURSIDE WA 6000</p>
  </footer>
  <div class="page__baseline"></div>
</section>

</body>
</html>
```